Accountants Stationary Package

Letter head, compliment slip, business card, report cover

Using selected logo which will be supplied when available design with compliment slip, letter head, business card and report cover. Some information to be amended and will be supplied at revision stage, design needs to resonate with chosen logo.

Update information 1 business card - my name is "Martin Kessler" post numerals are FCA , TITLE = Managing Director, (but maybe chartered accountant) is ok, my personal mobile is 0417 58 63 14 and personal email ids martin.k@kesslerledger.com,au, I like the tag line included " everybody ....succcess" Don't want professional liability logo but ok with the PQ and tallo logo I like the colours I like the blue back where it has a soft watermark finish 2. letterheads Need logos for tallo, PQ, professional standards Needs full company name and ABN NUMmber as - Kessler Ledger Pty Limited, ACN 748 206 513 Linked in ? I am also ok with initials instead of icons for phone, email, fax mobile, etc

Industry/Entity Type

Accounting

Requirements
Must have
• Kessler Ledger Pty Limited
• ABN 480591736
• Charted accountants
• Telephone 612 48350926
• Fax 612 4859 0417
• Po Box 6841, Kincumber, NSW, 2251
• Mobile 0417 586 314
• Address 42 Wenlock road, Kincumber, suite 9 Wenlock Central
• Mail@kesslerledger.com.au
• Website kesslerledger.com.au
• List of services;
• Tax and Accounting
• Business Development
• Superannuation and Financial Services

```html
<!DOCTYPE html>
<html lang="en">
<head>
<meta charset="utf-8">
<title>Kessler Ledger Letterhead</title>
<link href="https://fonts.googleapis.com/css2?family=Open+Sans:wght@400;700&display=swap" rel="stylesheet">
<style>
  :root {
    --bg: #9ec3e2;
    --paper: #ffffff;
    --blue: #1a8fc9;
    --blue-dark: #0f6fa3;
    --grey-line: #9a9a9a;
    --grey-text: #6d6d6d;
    --grey-head: #555555;
    --orange: #f0602a;
    --green: #3aa64a;
    --swoosh: #e9ebee;
  }
  html, body {
    margin: 0;
    padding: 0;
    width: 1200px;
    height: 784px;
    overflow: hidden;
    background: var(--bg);
    font-family: "Open Sans", Arial, sans-serif;
  }
  .letterhead {
    position: absolute;
    left: 330px;
    top: 10px;
    width: 540px;
    height: 764px;
    background: var(--paper);
    overflow: hidden;
    box-shadow: 0 4px 14px rgba(30, 70, 110, 0.25);
  }
  .decor { position: absolute; left: 0; top: 0; }
  .brand {
    position: absolute;
    left: 44px;
    top: 30px;
    display: flex;
    align-items: center;
    gap: 8px;
  }
  .brand-mark {
    width: 16px;
    height: 16px;
    background: var(--blue);
  }
  .brand-name {
    font-size: 20px;
    font-weight: 700;
    color: var(--blue);
    letter-spacing: 0.5px;
  }
  .tagline {
    position: absolute;
    left: 68px;
    top: 58px;
    font-size: 7px;
    color: var(--orange);
  }
  .footer {
    position: absolute;
    left: 0;
    bottom: 10px;
    width: 540px;
    height: 110px;
    font-size: 9px;
    color: var(--grey-text);
  }
  .col { position: absolute; top: 8px; }
  .col h3 {
    margin: 0 0 5px;
    font-size: 9.5px;
    font-weight: 700;
    color: var(--grey-head);
  }
  .col ul { list-style: none; margin: 0; padding: 0; }
  .col li { line-height: 12px; position: relative; padding-left: 11px; white-space: nowrap; }
  .col li svg { position: absolute; left: 0; top: 2px; }
  .col-services { left: 26px; }
  .col-locations { left: 150px; }
  .col-contact { left: 315px; }
  .col-email { left: 405px; }
</style>
</head>
<body>
<div class="letterhead">
  <svg class="decor" width="540" height="764" viewBox="0 0 540 764">
    <defs>
      <linearGradient id="footerShade" x1="0" y1="0" x2="0" y2="1">
        <stop offset="0" stop-color="#ffffff"/>
        <stop offset="1" stop-color="#f2f3f5"/>
      </linearGradient>
    </defs>
    <rect x="18" y="38" width="20" height="3" fill="var(--grey-line)"/>
    <rect x="210" y="64" width="330" height="4" fill="var(--blue)"/>
    <path d="M0 560 C60 600 180 640 540 650 L540 764 L0 764 Z" fill="url(#footerShade)"/>
    <path d="M0 600 C40 640 140 660 330 650 C200 668 60 660 0 630 Z" fill="var(--swoosh)"/>
    <path d="M0 640 C80 668 250 676 540 662" stroke="#e3e5e8" stroke-width="2" fill="none"/>
    <rect x="0" y="653" width="540" height="1" fill="var(--grey-line)"/>
    <rect x="22" y="648" width="2" height="11" fill="var(--orange)"/>
    <rect x="146" y="648" width="2" height="11" fill="var(--orange)"/>
    <rect x="311" y="648" width="2" height="11" fill="var(--orange)"/>
    <rect x="401" y="648" width="2" height="11" fill="var(--orange)"/>
    <rect x="520" y="648" width="2" height="11" fill="var(--orange)"/>
    <rect x="0" y="754" width="540" height="10" fill="var(--blue)"/>
    <rect x="0" y="762" width="540" height="2" fill="var(--blue-dark)"/>
  </svg>

  <div class="brand">
    <span class="brand-mark"></span>
    <span class="brand-name">KESSLER LEDGER</span>
  </div>
  <div class="tagline">every figure matters to your growth</div>

  <div class="footer">
    <div class="col col-services">
      <h3>Services</h3>
      <ul>
        <li><svg width="7" height="7"><path d="M0 0 L7 3.5 L0 7 Z" fill="var(--green)"/></svg>Tax and Accounting</li>
        <li><svg width="7" height="7"><path d="M0 0 L7 3.5 L0 7 Z" fill="var(--green)"/></svg>Business Development</li>
        <li><svg width="7" height="7"><path d="M0 0 L7 3.5 L0 7 Z" fill="var(--green)"/></svg>Superannuation and</li>
        <li>Financial Services</li>
      </ul>
    </div>
    <div class="col col-locations">
      <h3>Consulting locations</h3>
      <ul>
        <li><svg width="7" height="7"><path d="M0 0 L7 3.5 L0 7 Z" fill="var(--green)"/></svg>42 Wenlock road, Kincumber, suite 9</li>
        <li>Wenlock Central</li>
        <li><svg width="7" height="7"><path d="M0 0 L7 3.5 L0 7 Z" fill="var(--green)"/></svg>Po Box 6841, Kincumber, NSW, 2251</li>
      </ul>
    </div>
    <div class="col col-contact">
      <h3>Contact</h3>
      <ul>
        <li><svg width="8" height="8"><circle cx="4" cy="4" r="3.5" fill="none" stroke="var(--green)"/><text x="4" y="6" font-size="5" text-anchor="middle" fill="var(--green)">T</text></svg>612 4835 0926</li>
        <li><svg width="8" height="8"><circle cx="4" cy="4" r="3.5" fill="none" stroke="var(--green)"/><text x="4" y="6" font-size="5" text-anchor="middle" fill="var(--green)">F</text></svg>612 4859 0417</li>
        <li><svg width="8" height="8"><circle cx="4" cy="4" r="3.5" fill="none" stroke="var(--green)"/><text x="4" y="6" font-size="5" text-anchor="middle" fill="var(--green)">M</text></svg>0417 586 314</li>
      </ul>
    </div>
    <div class="col col-email">
      <h3>E-mail</h3>
      <ul>
        <li><svg width="8" height="8"><circle cx="4" cy="4" r="3.5" fill="none" stroke="var(--green)"/><text x="4" y="6" font-size="5" text-anchor="middle" fill="var(--green)">@</text></svg>Mail@kesslerledger.com.au</li>
        <li><svg width="8" height="8"><circle cx="4" cy="4" r="3.5" fill="none" stroke="var(--green)"/><text x="4" y="6" font-size="5" text-anchor="middle" fill="var(--green)">W</text></svg>www.kesslerledger.com.au</li>
        <li>ABN 00 000 000 000</li>
      </ul>
    </div>
  </div>
</div>
</body>
</html>
```